Sports medicine multidisciplinary brochures

Multi-disciplinary sports medicine clinic. Need a range of pamphlet / foldable brochures to advertise our various services. Looking at keeping a similar 'look' between the various brochures to still ID as being part of the group, but perhaps slight colour variation / different front pic to distinguish them. Looking at a pamphlet for: 1) General clinic (about us) info 2) Concussion info 3) Podiatry 4) Sports Physicians 5) Exercise Physiology 6) Osteoarthritis 7) Physiotherapy. Modern feel, but still warm / inviting. See attached logo / cards / etc. Thank you!

Target Market(s)

Athletes, sports injuries + general health / medical

Industry/Entity Type

Clinic

Requirements
Nice to have
• Simple, warm design. Activity / health / lifestyle related feel.
• Design to allow easy adaptation of wording / content.

```html
<!DOCTYPE html>
<html lang="en">
<head>
<meta charset="utf-8">
<title>Sports Physicians – Brochure Inside Spread</title>
<link href="https://fonts.googleapis.com/css2?family=Montserrat:wght@400;500;700&display=swap" rel="stylesheet">
<style>
  :root {
    --page-bg: #e6e6e6;
    --paper: #f6f6f6;
    --ink: #1d1d1d;
    --accent-orange: #e8650f;
    --accent-green: #1f945a;
    --white: #ffffff;
    --photo-light: #8ea3b5;
    --photo-dark: #3e4238;
  }
  * { box-sizing: border-box; margin: 0; padding: 0; }
  html, body {
    width: 1200px; height: 960px; overflow: hidden;
    background: var(--page-bg);
    font-family: 'Montserrat', sans-serif;
    color: var(--ink);
  }
  .spread {
    position: absolute; left: 20px; top: 64px;
    width: 1160px; height: 831px;
    display: flex;
    background: var(--paper);
  }
  .panel { position: relative; height: 100%; }
  .panel--left { width: 312px; padding: 36px 33px 0 33px; }
  .panel--photo { width: 544px; }
  .panel--right { width: 304px; padding: 34px 32px 0 33px; }

  .photo {
    width: 100%; height: 100%;
    background: linear-gradient(180deg, var(--photo-light) 0%, var(--photo-dark) 100%);
  }

  .heading {
    color: var(--accent-orange);
    font-weight: 700;
    font-size: 14.5px;
    line-height: 17px;
    text-transform: uppercase;
    margin-bottom: 14px;
  }
  .subheading {
    color: var(--accent-orange);
    font-weight: 700;
    font-size: 10.8px;
    line-height: 13px;
    margin-bottom: 12px;
  }
  .body-text {
    font-size: 10.8px;
    line-height: 13px;
    text-align: justify;
  }
  .bullets {
    list-style: none;
    font-size: 10.8px;
    line-height: 13px;
    text-align: justify;
    margin-bottom: 18px;
  }
  .bullets li { position: relative; padding-left: 14px; }
  .bullets li::before { content: "•"; position: absolute; left: 0; }
  .panel--left .bullets { margin-bottom: 20px; }
  .panel--right .bullets { margin-bottom: 16px; }

  .feature-box {
    position: absolute;
    left: 586px; top: 574px;
    width: 574px; height: 220px;
    background: var(--accent-green);
    color: var(--white);
    padding: 50px 32px 0 32px;
  }
  .feature-box__title {
    font-weight: 700;
    font-size: 14.5px;
    text-transform: uppercase;
    margin-bottom: 16px;
  }
  .feature-box__text {
    font-size: 10.8px;
    line-height: 13px;
    text-align: justify;
  }
</style>
</head>
<body>
  <div class="spread">
    <section class="panel panel--left">
      <h2 class="heading">What is the difference between a sports physician and an orthopaedic surgeon?</h2>
      <p class="body-text">Both are well trained in musculoskeletal medicine, but CSEM fellows specialize in the non-operative treatment of these conditions while surgeons specialize in the performance of the operation. However, approximately 90% of musculoskeletal injuries are non-surgical, and the CSEM fellow can help maximize and tailor non-operative treatment, guide appropriate rehab programs and therapies, and when necessary expedite referral to our surgical colleagues. In addition, extensive training is also undertaken in broader disciplines such as:</p>
      <ul class="bullets">
        <li>Concussion and other head injuries</li>
        <li>Diagnostic and interventional use of ultrasound to guide treatment</li>
        <li>Athletes with acute or chronic illness (including diabetes, asthma)</li>
        <li>Nutrition, supplements, and performance optimization</li>
        <li>Exercise prescription for those wanting to increase their fitness and focus on preventative health</li>
        <li>Injury prevention</li>
        <li>“Return to play” decisions</li>
        <li>Healthy lifestyle promotion</li>
      </ul>
      <h2 class="heading">Do sports physicians only treat competitive athletes?</h2>
      <p class="body-text">No, our specialists are ideal physicians for the non-athlete as well, and are excellent resources for the individual who wishes to become active or begin an exercise program. For the “weekend warrior” or worker experiences an injury, the same expertise used for the competitive athlete can be applied to return you as quickly as possible to full function. In addition, as some of our specialists have also a second qualification as a general practitioner (CGPA), a referral is not needed to see us. So unlike other specialist physicians you can see us directly.</p>
    </section>

    <section class="panel panel--photo">
      <div class="photo" role="img" aria-label="Photo of a woman in a teal tank top running on an outdoor athletics track"></div>
    </section>

    <section class="panel panel--right">
      <h3 class="subheading">CSEM fellows often act as the primary contact for elite sports teams and athletes:</h3>
      <ul class="bullets">
        <li>Assessing and diagnosing injuries or illness</li>
        <li>Close integration with the team and understanding demands of training and the game</li>
        <li>Devising and coordinating a comprehensive management program</li>
        <li>Understanding the intricacies of drug testing in elite settings, and the unique physiological demands on high demand athletes</li>
        <li>Ensuring your injury is corrected, but also to help ensure once you return to your sport that you stay playing your sport – prevention programs are integral to our practice</li>
      </ul>
      <h3 class="subheading">CSEM fellows also have extensive competency in “exercise is medicine”</h3>
      <ul class="bullets">
        <li>Management of the ‘lifestyle’ diseases in our community, such as diabetes, osteoarthritis, and heart disease and integration of our “exercise is medicine” approach</li>
        <li>Non-surgical management of musculoskeletal injuries such as Achilles tendonopathy, plantar fasciitis, tennis elbow, and osteoarthritis</li>
        <li>Dive and altitude medicine</li>
        <li>Medical screenings and health assessments, including on-site ECG’s and spirometry</li>
        <li>Travel medicine and vaccinations</li>
      </ul>
    </section>

    <div class="feature-box">
      <h2 class="feature-box__title">What is a sports physician specialist?</h2>
      <p class="feature-box__text">Sport and Exercise Physicians (CSEM) are doctors with specialist training in the management of musculoskeletal injuries and illnesses to maximize function and minimize disability and time away from your sport, work, or school. After graduating from medical school, a minimum of a further 7 years is required along with various examination and research requirements to gain a CSEM fellowship.</p>
    </div>
  </div>
</body>
</html>
```